Map of the world with destinations for the website

Our company organizes sailing trips in 17 different spots in the world: 12 in Europe, 3 in the Caribbean, 1 in Thailand, 1 in the Seychelles. In every spot there are 1 - 10 different dates of trips in one year.
We need a map of the world for our website http://sail-with-anchora.com/segeltoerns, that will show all spots where our trips take place - all spots on one map. After you clicked on one spot, you should see a small window with basic information about the trips: all dates, prices, duration in days, places available. After another click you will be directed to the offer.
The file should be static: just a jpg-file with the map and one window with informations.
On 1. november we launch about 100 new trips, that should be nicely presented on the map.
We have already started to work on this. You can develop the map we created so far (attached to this task) or create a new one.

```html
<!DOCTYPE html>
<html lang="de">
<head>
<meta charset="utf-8">
<title>Anchora – Segeltörns: Alle Termine</title>
<link href="https://fonts.googleapis.com/css2?family=Roboto+Condensed:wght@400;700&family=Signika:wght@300;400;600&display=swap" rel="stylesheet">
<style>
:root{
  --navy:#0d2e63;
  --navy-deep:#0a2554;
  --nav:#114a8a;
  --nav-light:#1d64a8;
  --sea-top:#e9eef3;
  --sea-mid:#8db6d9;
  --sea-deep:#2f7bbb;
  --land:#d7d9dc;
  --white:#ffffff;
  --ink:#3c4048;
  --ink-soft:#5d636c;
  --orange:#f5a31a;
  --red:#e1402a;
  --badge:#0e2f61;
  --side-bg:#f2f4f6;
}
*{box-sizing:border-box;margin:0;padding:0}
html,body{width:976px;height:1200px;overflow:hidden}
body{background:var(--navy);font-family:"Signika",sans-serif;color:var(--ink);position:relative}
.page-frame{position:absolute;left:59px;top:0;width:859px;height:1145px;background:var(--navy-deep)}

/* navigation */
.main-nav{position:absolute;left:67px;top:15px;width:839px;height:35px;display:flex;background:linear-gradient(#1b5d9f,#0f4480)}
.main-nav a{color:var(--white);text-decoration:none;font-family:"Roboto Condensed",sans-serif;font-size:16px;display:flex;align-items:center;justify-content:center;border-right:1px solid #0a3466;border-left:1px solid #2a6fb0}
.main-nav .brand{width:116px;font-family:"Signika",sans-serif;font-size:14px;font-weight:600;gap:5px}
.brand .mark{width:10px;height:10px;border-radius:50%;background:var(--orange)}
.main-nav .item{width:115px}
.main-nav .item.active{background:linear-gradient(#2670b5,#175795)}
.main-nav .icon{width:47px}
.main-nav .lang{width:48px}

/* breadcrumb */
.crumbs{position:absolute;left:67px;top:59px;width:839px;height:23px;background:var(--white);display:flex;align-items:center;font-size:11.5px}
.crumb{position:relative;height:100%;display:flex;align-items:center;padding:0 16px}
.crumb:first-child{width:105px;padding-left:17px;color:var(--ink-soft)}
.crumb.current{font-weight:600;color:var(--ink);padding-left:23px;width:125px}
.crumb svg{position:absolute;right:-8px;top:0}

/* sidebar */
.destinations{position:absolute;left:67px;top:92px;width:142px;list-style:none}
.destinations li{height:47.8px;display:flex;align-items:center;background:var(--white);border-bottom:1.5px solid var(--navy-deep);font-size:11.5px;line-height:14px;color:var(--ink)}
.destinations li.head{background:#dde3ea;font-size:13px}
.thumb{width:46px;height:100%;flex:none;margin-right:7px}
.destinations li.head .thumb{background:linear-gradient(#6f9ccc,#2a5f9b);display:flex;align-items:center;justify-content:center}

/* world map */
.world-map{position:absolute;left:218px;top:92px;width:688px;height:307px;overflow:hidden;background:radial-gradient(ellipse at 55% 35%,var(--land) 0%,#cfd4d9 40%,transparent 62%),linear-gradient(180deg,var(--sea-top) 0%,var(--sea-mid) 55%,var(--sea-deep) 100%)}
.pin{position:absolute;transform:translate(-50%,-100%)}
.map-label{position:absolute;font-size:12px;color:#3d4047;white-space:nowrap}
.map-label.big{font-size:20px;color:#4a4d55}
.map-label.light{color:#1d2733}
.countdown{position:absolute;right:9px;top:9px;display:flex;align-items:center;gap:8px;font-size:12.5px;font-weight:600;color:#2b2f36}
.countdown .timer{display:flex;background:#2a7ad0;border:1px solid #fff}
.countdown .timer span{color:#fff;font-weight:300;font-size:13px;padding:1px 6px;border-left:1px solid #8fc0ee}
.countdown .timer span:first-child{border-left:0}
.countdown small{font-size:8px}
.legend{position:absolute;left:27px;top:254px}
.legend div{width:162px;height:16px;background:rgba(110,120,130,.75);color:#fff;font-size:12px;display:flex;align-items:center;gap:8px;padding-left:4px;margin-bottom:5px;letter-spacing:.3px}

/* content */
.content{position:absolute;left:218px;top:399px;width:688px;height:738px;background:var(--white)}
.region-map{position:absolute;left:27px;top:30px;width:271px;height:186px;border:1px solid #9aa;box-shadow:0 2px 4px rgba(0,0,0,.35);background:radial-gradient(ellipse at 30% 25%,#d9dbde 0%,#d3d6da 35%,transparent 55%),linear-gradient(180deg,#c9ccd0 0%,#8fb8dc 50%,#3a86c6 100%);overflow:hidden}
.region-map .map-label{font-size:10px}
.region-map .map-label.big{font-size:16px}
.photo{position:absolute;left:316px;top:30px;width:347px;height:186px;box-shadow:0 2px 4px rgba(0,0,0,.35);background:linear-gradient(180deg,#8d9bab 0%,#9c8a72 30%,#5f8f93 50%,#2c8fa3 75%,#177e93 100%)}
.photo svg{position:absolute;top:50%;transform:translateY(-50%)}
.trip-title{position:absolute;left:46px;top:240px;font-size:21px;font-weight:300;color:#3a3e44}
.trip-text{position:absolute;left:46px;top:270px;font-size:12px;font-weight:300;color:#3a3e44;letter-spacing:.3px}
.sort{position:absolute;left:45px;top:316px;display:flex;align-items:center;gap:8px;font-size:12.5px;font-weight:300}
.select{width:158px;height:19px;border:1px solid #c9cdd2;border-radius:3px;background:linear-gradient(#fff,#ececec);font-size:13px;font-weight:400;padding:1px 7px;position:relative}
.select svg{position:absolute;right:4px;top:4px}

.dates{position:absolute;left:45px;top:354px;border-collapse:collapse;font-size:12.5px;font-weight:300;color:#3a3e44}
.dates th{font-weight:600;text-align:left;font-size:13px;height:23px;white-space:nowrap}
.dates td{height:23.5px;white-space:nowrap;padding:0}
.c-date{width:119px}.c-days{width:41px}.c-price{width:62px}.c-area{width:166px}.c-boat{width:130px}
.help{display:inline-block;width:12px;height:12px;border-radius:50%;background:var(--badge);color:#fff;font-size:9px;text-align:center;line-height:12px;vertical-align:1px;margin-left:2px}
.tag{display:inline-block;width:25px;height:13px;font-size:9.5px;font-weight:600;line-height:13px;padding-left:3px;margin-right:4px;clip-path:polygon(0 0,78% 0,100% 50%,78% 100%,0 100%);vertical-align:middle}
.tag.full{background:var(--badge);color:#fff}
.tag.free{background:linear-gradient(90deg,#e8ecf1,#fff);color:var(--badge);border-left:2px solid var(--badge)}

/* footer */
.footer{position:absolute;left:67px;top:1159px;width:839px;height:33px;background:#14457f;display:flex;align-items:center;color:#fff}
.newsletter{display:flex;align-items:center;gap:5px;padding-left:9px;font-family:"Roboto Condensed",sans-serif;font-size:15px}
.newsletter .q{width:13px;height:13px;border:1px solid #fff;border-radius:50%;font-size:9px;text-align:center;line-height:11px}
.newsletter input{width:104px;height:19px;border:0;font-size:8px;padding-left:4px;color:#aaa;font-family:"Signika",sans-serif;margin-left:3px}
.newsletter .go{width:18px;height:19px;background:#2a67a8;display:flex;align-items:center;justify-content:center}
.social{margin-left:auto;display:flex;align-items:center;gap:8px;padding-right:12px}
.like{display:flex;gap:3px;font-size:8px}
.like span{background:#eef1f5;color:#3a4f7a;border:1px solid #c6ccd6;padding:1px 4px;border-radius:2px}
.social .square{width:24px;height:24px;background:#3c66b0;border-radius:3px}
.social .square.red{background:#c8302a}
.sitemap{font-family:"Roboto Condensed",sans-serif;font-size:15px;border-left:1px solid #2b62a0;padding:0 12px 0 12px;height:100%;display:flex;align-items:center;gap:6px}
</style>
</head>
<body>
<div class="page-frame"></div>

<nav class="main-nav">
  <a class="brand" href="#"><span class="mark"></span>Anchora</a>
  <a class="item active" href="#">Segeltörns</a>
  <a class="item" href="#">Bilder</a>
  <a class="item" href="#">Infos</a>
  <a class="item" href="#">Über uns</a>
  <a class="item" href="#">Blog</a>
  <a class="icon" href="#" aria-label="Login"><svg width="14" height="18" viewBox="0 0 14 18"><path d="M3 8V5a4 4 0 0 1 8 0v3" fill="none" stroke="#fff" stroke-width="2"/><rect x="1" y="8" width="12" height="9" rx="1" fill="#fff"/></svg></a>
  <a class="icon" href="#" aria-label="Suche"><svg width="22" height="20" viewBox="0 0 22 20"><circle cx="14" cy="7" r="5.5" fill="none" stroke="#fff" stroke-width="2"/><path d="M10 11l-7 7" stroke="#fff" stroke-width="3"/></svg></a>
  <a class="lang" href="#">DE</a>
</nav>

<div class="crumbs">
  <div class="crumb">Segeltörns<svg width="14" height="23" viewBox="0 0 14 23"><path d="M1 0l11 11.5L1 23" fill="none" stroke="#0d2e63" stroke-width="4"/></svg></div>
  <div class="crumb current">Alle Termine<svg width="14" height="23" viewBox="0 0 14 23"><path d="M1 0l11 11.5L1 23" fill="none" stroke="#0d2e63" stroke-width="4"/></svg></div>
</div>

<ul class="destinations">
  <li class="head"><span class="thumb"><svg width="26" height="38" viewBox="0 0 26 38"><path d="M13 1a11 11 0 0 1 11 11c0 8-11 20-11 20S2 20 2 12A11 11 0 0 1 13 1z" fill="#0d2e63" stroke="#fff" stroke-width="1.5"/><ellipse cx="13" cy="35" rx="9" ry="2" fill="#0d2e63"/></svg></span>Sailing Trips</li>
  <li><span class="thumb" role="img" aria-label="Foto: Stege am Wasser" style="background:linear-gradient(#d9a06a,#4b86b8)"></span>Dänische<br>Südsee</li>
  <li><span class="thumb" role="img" aria-label="Foto: Segelboot vor Küste" style="background:linear-gradient(#9bc3e2,#2f7fb0)"></span>Griechenland:<br>Athen - Rhodos</li>
  <li><span class="thumb" role="img" aria-label="Foto: Boote im Hafen" style="background:linear-gradient(#6fa7d3,#2c6e9f)"></span>Griechenland:<br>Dodekanes Süd</li>
  <li><span class="thumb" role="img" aria-label="Foto: Yachthafen" style="background:linear-gradient(#8ca4bf,#3e6b92)"></span>Griechenland:<br>Saronischer Golf</li>
  <li><span class="thumb" role="img" aria-label="Foto: Skipper mit Fernglas" style="background:linear-gradient(#a9bfd6,#5a6d84)"></span>Griechenland:<br>Skipper-<br>Training</li>
  <li><span class="thumb" role="img" aria-label="Foto: Segelboot unter Segeln" style="background:linear-gradient(#c7d5e2,#4d6c8c)"></span>Italien:<br>Elba</li>
  <li><span class="thumb" role="img" aria-label="Foto: Katamaran auf dem Meer" style="background:linear-gradient(#7fb2dd,#2b79b9)"></span>Karibik:<br>Leewards</li>
  <li><span class="thumb" role="img" aria-label="Foto: Crew an Deck" style="background:linear-gradient(#d8a24a,#5a8fbf)"></span>Karibik:<br>Windwards</li>
  <li><span class="thumb" role="img" aria-label="Foto: Entspannen an Bord" style="background:linear-gradient(#c84b3e,#d8a07a)"></span>Kroatien:<br>Burnout-Auszeit</li>
  <li><span class="thumb" role="img" aria-label="Foto: Altstadtdächer" style="background:linear-gradient(#b8643f,#8a4a32)"></span>Kroatien:<br>Nach Dubrovnik</li>
  <li><span class="thumb" role="img" aria-label="Foto: Strand" style="background:linear-gradient(#a9c9e3,#d8cdb8)"></span>Kuba:<br>Südküste</li>
  <li><span class="thumb" role="img" aria-label="Foto: Palmenstrand" style="background:linear-gradient(#b7d9ef,#6aa56a)"></span>Seychellen</li>
  <li><span class="thumb" role="img" aria-label="Foto: Segelboot in Bucht" style="background:linear-gradient(#8fbde3,#2f78b2)"></span>Spanien:<br>Balearen</li>
  <li><span class="thumb" role="img" aria-label="Foto: Vulkanküste" style="background:linear-gradient(#9fbcd6,#5e6f7c)"></span>Spanien:<br>Kanaren</li>
  <li><span class="thumb" role="img" aria-label="Foto: Felsen in Bucht" style="background:linear-gradient(#cbd7de,#6b8a78)"></span>Thailand:<br>Andamanensee</li>
  <li><span class="thumb" role="img" aria-label="Foto: Sonnenuntergang" style="background:linear-gradient(#f0c36a,#8a6a4a)"></span>Türkei:<br>Burnout-Auszeit</li>
  <li><span class="thumb" role="img" aria-label="Foto: Sprung ins Meer" style="background:linear-gradient(#a9c5d9,#3f88b2)"></span>Türkei:<br>Lykische Küste</li>
</ul>

<section class="world-map" role="img" aria-label="Weltkarte mit allen Segelrevieren">
  <div class="countdown">Unsere Frühbucher-Aktion endet bald
    <div class="timer"><span>12<small>t</small></span><span>15<small>h</small></span><span>34<small>m</small></span></div>
  </div>

  <svg class="pin" style="left:356px;top:44px" width="14" height="20" viewBox="0 0 14 20"><path d="M7 20C5 13 0 11 0 7a7 7 0 0 1 14 0c0 4-5 6-7 13z" fill="#f5a31a"/></svg>
  <svg class="pin" style="left:376px;top:92px" width="14" height="20" viewBox="0 0 14 20"><path d="M7 20C5 13 0 11 0 7a7 7 0 0 1 14 0c0 4-5 6-7 13z" fill="#f5a31a"/></svg>
  <svg class="pin" style="left:381px;top:94px" width="14" height="20" viewBox="0 0 14 20"><path d="M7 20C5 13 0 11 0 7a7 7 0 0 1 14 0c0 4-5 6-7 13z" fill="#f5a31a"/></svg>
  <svg class="pin" style="left:361px;top:99px" width="14" height="20" viewBox="0 0 14 20"><path d="M7 20C5 13 0 11 0 7a7 7 0 0 1 14 0c0 4-5 6-7 13z" fill="#f5a31a"/></svg>
  <svg class="pin" style="left:342px;top:106px" width="14" height="20" viewBox="0 0 14 20"><path d="M7 20C5 13 0 11 0 7a7 7 0 0 1 14 0c0 4-5 6-7 13z" fill="#f5a31a"/></svg>
  <svg class="pin" style="left:394px;top:122px" width="14" height="20" viewBox="0 0 14 20"><path d="M7 20C5 13 0 11 0 7a7 7 0 0 1 14 0c0 4-5 6-7 13z" fill="#f5a31a"/></svg>
  <svg class="pin" style="left:399px;top:122px" width="14" height="20" viewBox="0 0 14 20"><path d="M7 20C5 13 0 11 0 7a7 7 0 0 1 14 0c0 4-5 6-7 13z" fill="#f5a31a"/></svg>
  <svg class="pin" style="left:404px;top:122px" width="14" height="20" viewBox="0 0 14 20"><path d="M7 20C5 13 0 11 0 7a7 7 0 0 1 14 0c0 4-5 6-7 13z" fill="#f5a31a"/></svg>
  <svg class="pin" style="left:409px;top:122px" width="14" height="20" viewBox="0 0 14 20"><path d="M7 20C5 13 0 11 0 7a7 7 0 0 1 14 0c0 4-5 6-7 13z" fill="#f5a31a"/></svg>
  <svg class="pin" style="left:414px;top:122px" width="18" height="26" viewBox="0 0 14 20"><path d="M7 20C5 13 0 11 0 7a7 7 0 0 1 14 0c0 4-5 6-7 13z" fill="#f5a31a"/></svg>
  <svg class="pin" style="left:283px;top:143px" width="14" height="20" viewBox="0 0 14 20"><path d="M7 20C5 13 0 11 0 7a7 7 0 0 1 14 0c0 4-5 6-7 13z" fill="#e1402a"/></svg>
  <svg class="pin" style="left:88px;top:169px" width="14" height="20" viewBox="0 0 14 20"><path d="M7 20C5 13 0 11 0 7a7 7 0 0 1 14 0c0 4-5 6-7 13z" fill="#e1402a"/></svg>
  <svg class="pin" style="left:137px;top:178px" width="14" height="20" viewBox="0 0 14 20"><path d="M7 20C5 13 0 11 0 7a7 7 0 0 1 14 0c0 4-5 6-7 13z" fill="#e1402a"/></svg>
  <svg class="pin" style="left:149px;top:187px" width="14" height="20" viewBox="0 0 14 20"><path d="M7 20C5 13 0 11 0 7a7 7 0 0 1 14 0c0 4-5 6-7 13z" fill="#e1402a"/></svg>
  <svg class="pin" style="left:615px;top:198px" width="14" height="20" viewBox="0 0 14 20"><path d="M7 20C5 13 0 11 0 7a7 7 0 0 1 14 0c0 4-5 6-7 13z" fill="#e1402a"/></svg>
  <svg class="pin" style="left:480px;top:257px" width="14" height="20" viewBox="0 0 14 20"><path d="M7 20C5 13 0 11 0 7a7 7 0 0 1 14 0c0 4-5 6-7 13z" fill="#e1402a"/></svg>

  <span class="map-label" style="left:336px;top:49px">Deuchland</span>
  <span class="map-label" style="left:386px;top:65px">Croatia</span>
  <span class="map-label" style="left:309px;top:103px">Spain</span>
  <span class="map-label" style="left:354px;top:103px">Italy</span>
  <span class="map-label big" style="left:424px;top:99px">Greece</span>
  <span class="map-label" style="left:295px;top:133px">Santa Cruz</span>
  <span class="map-label" style="left:81px;top:179px">Carribbean</span>
  <span class="map-label" style="left:606px;top:160px">Thailand</span>
  <span class="map-label light" style="left:501px;top:254px">Seychelles</span>

  <div class="legend">
    <div><svg width="11" height="15" viewBox="0 0 14 20"><path d="M7 20C5 13 0 11 0 7a7 7 0 0 1 14 0c0 4-5 6-7 13z" fill="#e1402a"/></svg>Winter Trips</div>
    <div><svg width="11" height="15" viewBox="0 0 14 20"><path d="M7 20C5 13 0 11 0 7a7 7 0 0 1 14 0c0 4-5 6-7 13z" fill="#f5a31a"/></svg>Summer Trips</div>
  </div>
</section>

<main class="content">
  <div class="region-map" role="img" aria-label="Karte der griechischen Inseln mit Stationen des Törns">
    <svg class="pin" style="left:63px;top:82px" width="14" height="20" viewBox="0 0 14 20"><path d="M7 20C5 13 0 11 0 7a7 7 0 0 1 14 0c0 4-5 6-7 13z" fill="#f5a31a"/></svg>
    <svg class="pin" style="left:100px;top:99px" width="14" height="20" viewBox="0 0 14 20"><path d="M7 20C5 13 0 11 0 7a7 7 0 0 1 14 0c0 4-5 6-7 13z" fill="#f5a31a"/></svg>
    <svg class="pin" style="left:158px;top:97px" width="14" height="20" viewBox="0 0 14 20"><path d="M7 20C5 13 0 11 0 7a7 7 0 0 1 14 0c0 4-5 6-7 13z" fill="#f5a31a"/></svg>
    <svg class="pin" style="left:186px;top:120px" width="18" height="26" viewBox="0 0 14 20"><path d="M7 20C5 13 0 11 0 7a7 7 0 0 1 14 0c0 4-5 6-7 13z" fill="#f5a31a"/></svg>
    <svg class="pin" style="left:209px;top:107px" width="14" height="20" viewBox="0 0 14 20"><path d="M7 20C5 13 0 11 0 7a7 7 0 0 1 14 0c0 4-5 6-7 13z" fill="#f5a31a"/></svg>
    <svg class="pin" style="left:75px;top:138px" width="14" height="20" viewBox="0 0 14 20"><path d="M7 20C5 13 0 11 0 7a7 7 0 0 1 14 0c0 4-5 6-7 13z" fill="#f5a31a"/></svg>
    <span class="map-label" style="left:10px;top:44px">GREECE</span>
    <span class="map-label" style="left:50px;top:90px">Gliada</span>
    <span class="map-label" style="left:88px;top:108px">Naxos</span>
    <span class="map-label" style="left:150px;top:108px">Kos</span>
    <span class="map-label" style="left:214px;top:104px">Fethiya</span>
    <span class="map-label big" style="left:186px;top:126px">Rhodos</span>
    <span class="map-label" style="left:84px;top:135px">Chania</span>
  </div>

  <div class="photo" role="img" aria-label="Foto: Sprung vom Segelboot ins türkisblaue Meer">
    <svg style="left:6px" width="12" height="24" viewBox="0 0 12 24"><path d="M10 2L2 12l8 10" fill="none" stroke="#fff" stroke-width="2"/></svg>
    <svg style="right:6px" width="12" height="24" viewBox="0 0 12 24"><path d="M2 2l8 10-8 10" fill="none" stroke="#fff" stroke-width="2"/></svg>
  </div>

  <h1 class="trip-title">Greece: Rhodos</h1>
  <p class="trip-text">Text here text herehere text herehere text herehere text herehere text herehere text herehere text here</p>

  <div class="sort">Sortieren nach:
    <div class="select">Datum<svg width="7" height="11" viewBox="0 0 7 11"><path d="M0 4l3.5-4L7 4zM0 7l3.5 4L7 7z" fill="#222"/></svg></div>
  </div>

  <table class="dates">
    <thead>
      <tr><th class="c-date">Datum</th><th class="c-days">Tage</th><th class="c-price">Preis <span class="help">?</span></th><th class="c-area">Segelrevier</th><th class="c-boat">Boote / Sprachen <span class="help">?</span></th><th>Strecke <span class="help">?</span></th></tr>
    </thead>
    <tbody>
      <tr><td>21.12. - 04.01.2014</td><td>14</td><td>1.250 €</td><td>Karibik: Windwards</td><td><span class="tag full">DE</span><span class="tag full">DE</span><span class="tag free">DE</span></td><td>300 sm</td></tr>
      <tr><td>27.12. - 06.01.2014</td><td>10</td><td>ab 1.130 €</td><td>Thailand: Andamanensee</td><td><span class="tag full">DE</span><span class="tag full">DE</span><span class="tag free">DE</span></td><td>230 sm</td></tr>
      <tr><td>01.02. - 15.02.2014</td><td>14</td><td>1.150 €</td><td>Karibik: Leewards</td><td><span class="tag full">DE</span><span class="tag free">DE</span></td><td>350 sm</td></tr>
      <tr><td>01.02. - 08.02.2014</td><td>7</td><td>490 €</td><td>Spanien: Kanaren</td><td><span class="tag free">DE</span></td><td>220 sm</td></tr>
      <tr><td>08.02. - 22.02.2014</td><td>14</td><td>1.090 €</td><td>Karibik: Windwards</td><td><span class="tag full">DE</span><span class="tag free">DE</span></td><td>300 sm</td></tr>
      <tr><td>08.02. - 16.02.2014</td><td>8</td><td>560 €</td><td>Spanien: Kanaren</td><td><span class="tag free">DE</span></td><td>150 sm</td></tr>
      <tr><td>15.02. - 01.03.2014</td><td>14</td><td>1.180 €</td><td>Thailand: Andamanensee</td><td><span class="tag full">DE</span><span class="tag free">DE</span></td><td>290 sm</td></tr>
      <tr><td>01.03. - 11.03.2014</td><td>10</td><td>990 €</td><td>Thailand: Andamanensee</td><td><span class="tag free">DE</span><span class="tag free">DE</span></td><td>230 sm</td></tr>
      <tr><td>05.03. - 15.03.2014</td><td>10</td><td>610 €</td><td>Spanien: Kanaren</td><td><span class="tag free">DE</span></td><td>180 sm</td></tr>
      <tr><td>08.03. - 22.03.2014</td><td>14</td><td>1.090 €</td><td>Karibik: Windwards</td><td><span class="tag full">DE</span><span class="tag free">DE</span></td><td>300 sm</td></tr>
      <tr><td>15.03. - 22.03.2014</td><td>7</td><td>490 €</td><td>Spanien: Kanaren</td><td><span class="tag free">DE</span></td><td>220 sm</td></tr>
      <tr><td>12.04. - 26.04.2014</td><td>14</td><td>1.090 €</td><td>Kuba: Südküste</td><td><span class="tag free">DE</span></td><td>280 sm</td></tr>
      <tr><td>12.04. - 26.04.2014</td><td>14</td><td>1.070 €</td><td>Karibik: Leewards</td><td><span class="tag free">DE</span><span class="tag free">DE</span><span class="tag free">DE</span></td><td>350 sm</td></tr>
      <tr><td>12.04. - 26.04.2014</td><td>14</td><td>990 €</td><td>Karibik: Windwards</td><td><span class="tag free">DE</span><span class="tag free">DE</span><span class="tag free">DE</span></td><td>300 sm</td></tr>
    </tbody>
  </table>
</main>

<footer class="footer">
  <div class="newsletter"><span class="q">?</span>Newsletter<input type="text" value="E-Mail-Adresse" aria-label="E-Mail-Adresse"><span class="go"><svg width="7" height="10" viewBox="0 0 7 10"><path d="M0 0l7 5-7 5z" fill="#fff"/></svg></span></div>
  <div class="social">
    <div class="like"><span>Gefällt mir</span><span>1,8 Tsd.</span></div>
    <span class="square" aria-label="Soziales Netzwerk"></span>
    <span class="square red" aria-label="Videokanal"></span>
  </div>
  <div class="sitemap">Seitenüberblick<svg width="6" height="10" viewBox="0 0 6 10"><path d="M1 1l4 4-4 4" fill="none" stroke="#fff" stroke-width="2"/></svg></div>
</footer>
</body>
</html>
```